Aerial photo/video drone company needs new business card

Aerial visual company who offers photos and video services via drones.

We are QVL certified and work in the real estate, insurance, construction, and film industries.

I'm looking for a clean, professional, maybe even edgy design, that will be a conversation starter when networking.

I've included our logo, current business card, and font.

Our current business card is decent; albeit, I'm looking for something more unique. If you folks provide good designs, I'll definitely guarantee payment (and I'm not opposed to tipping if the design is above and beyond).

Target Market(s)

Insurance companies, real estate agents, construction companies, advertising & other creative agencies, and filmmakers/producers.

Industry/Entity Type

Business

Contact Information for Business Card

Company name pronounced air-a-vee.

Font styles to use
Other font styles liked:
• Font was uploaded; that or similar; not opposed to other fonts if they work well with the design

Requirements
Must have
• Clearly prominent logo; my name and title; phone number; email address; web address; mentioned "QVL Certified" or similar; should indicate "Aerial visual"
Nice to have
• Watermark of logo or otherwise
Should not have
• Pictures of drones or scenic shots

```html
<!DOCTYPE html>
<html lang="en">
<head>
<meta charset="utf-8">
<title>Skyvane Business Card</title>
<link rel="stylesheet" href="https://fonts.googleapis.com/css2?family=Montserrat:wght@400;500;600;700&display=swap">
<style>
  :root {
    --bg: #ece9e4;
    --card-dark: #2f3442;
    --card-light: #ffffff;
    --navy: #34425e;
    --sky: #4aa8dc;
    --grey-text: #7b7f87;
    --white-text: #f2f4f7;
  }
  * { margin: 0; padding: 0; box-sizing: border-box; }
  html, body {
    width: 1200px; height: 800px; overflow: hidden;
    background: var(--bg);
    font-family: "Montserrat", sans-serif;
  }
  .stage {
    width: 1200px; height: 800px;
    display: flex; align-items: center; justify-content: center; gap: 40px;
  }
  .card {
    width: 540px; height: 309px;
    border-radius: 18px;
    position: relative;
    box-shadow: 0 6px 18px rgba(0,0,0,0.12);
  }
  .card-front {
    background: var(--card-dark);
    display: flex; flex-direction: column; align-items: center; justify-content: center;
  }
  .brand {
    display: flex; align-items: center; gap: 14px;
  }
  .brand-mark {
    flex: none;
    border-radius: 50%;
  }
  .brand-name {
    font-weight: 700;
    letter-spacing: 1px;
    line-height: 1;
  }
  .card-front .brand-mark { width: 40px; height: 40px; background: var(--sky); }
  .card-front .brand-name { font-size: 64px; color: var(--sky); }
  .tagline {
    margin-top: 14px;
    font-size: 13px; font-weight: 600;
    color: var(--sky);
  }
  .industries {
    margin-top: 10px;
    font-size: 13px; font-weight: 600;
    color: var(--white-text);
    letter-spacing: 0.3px;
  }
  .industries .divider { margin: 0 8px; }
  .certification {
    margin-top: 12px;
    font-size: 11px; font-weight: 600;
    color: var(--sky);
    letter-spacing: 2px;
    text-transform: uppercase;
  }

  .card-back { background: var(--card-light); }
  .card-back .brand {
    position: absolute; left: 40px; bottom: 46px;
  }
  .card-back .brand-mark { width: 34px; height: 34px; background: var(--navy); }
  .card-back .brand-name { font-size: 52px; color: var(--navy); }
  .contact-block {
    position: absolute; right: 40px; top: 44px;
    text-align: left;
  }
  .person-name {
    font-size: 19px; font-weight: 600; color: var(--grey-text);
  }
  .person-title {
    margin-top: 4px;
    font-size: 14px; font-weight: 500; color: var(--sky);
  }
  .contact-list { list-style: none; margin-top: 18px; }
  .contact-list li {
    display: flex; align-items: center; gap: 10px;
    font-size: 13px; font-weight: 500; color: var(--grey-text);
    margin-bottom: 8px;
  }
  .contact-list svg { width: 13px; height: 13px; flex: none; }
</style>
</head>
<body>
<main class="stage">
  <section class="card card-front">
    <div class="brand">
      <span class="brand-mark" aria-hidden="true"></span>
      <span class="brand-name">skyvane</span>
    </div>
    <p class="tagline">Aerial Visual for</p>
    <p class="industries">Real Estate<span class="divider">|</span>Insurance<span class="divider">|</span>Construction<span class="divider">|</span>Film</p>
    <p class="certification">QVL Certified</p>
  </section>

  <section class="card card-back">
    <div class="contact-block">
      <p class="person-name">Daniel T. Marsh</p>
      <p class="person-title">Owner | sUAS Pilot</p>
      <ul class="contact-list">
        <li>
          <svg viewBox="0 0 16 16" aria-hidden="true"><rect x="1" y="3" width="14" height="10" rx="1" fill="#4aa8dc"/><path d="M1.5 3.5 8 9l6.5-5.5" stroke="#fff" stroke-width="1.3" fill="none"/></svg>
          dan@skyvane.com
        </li>
        <li>
          <svg viewBox="0 0 16 16" aria-hidden="true"><path d="M4 1.5h2.5l1 3.5-1.8 1.2a8 8 0 0 0 4.1 4.1L11 8.5l3.5 1V12a2 2 0 0 1-2 2A11 11 0 0 1 2 3.5a2 2 0 0 1 2-2z" fill="#4aa8dc"/></svg>
          555.014.2290
        </li>
        <li>
          <svg viewBox="0 0 16 16" aria-hidden="true"><circle cx="8" cy="8" r="6.5" fill="none" stroke="#4aa8dc" stroke-width="1.4"/><ellipse cx="8" cy="8" rx="2.8" ry="6.5" fill="none" stroke="#4aa8dc" stroke-width="1.2"/><path d="M1.5 8h13M2.5 5h11M2.5 11h11" stroke="#4aa8dc" stroke-width="1.1"/></svg>
          skyvane.com
        </li>
      </ul>
    </div>
    <div class="brand">
      <span class="brand-mark" aria-hidden="true"></span>
      <span class="brand-name">skyvane</span>
    </div>
  </section>
</main>
</body>
</html>
```